Generic Label Design for Kids Craft Kits

I'm starting a new online / retail business that will package different craft materials and instructions into craft projects for kids from ages 2-12. I need a label for the front of the packages that looks professional. Although I'm interested in a very professional design (the kits will not be sold at a low cost) I'm also aiming for a 'natural' / crafty look to my packaging. The packaging will be hand-made with Kraft boxes / bags as the basic material. I will be adding hand-made embellishments to make the packaging look attractive (ex: a paper or crochet flower will be used to seal the packaging and hand-made twine ropes will be used as the handle). On the back of the package, I will be using a custom-made rubber stamp to imprint my Logo and Website address. I've included some pictures of packaging material that I really liked
Updates

       Please see updated brief and new deadline, this should make the project much clearer and easier.

Target Market(s)

End user = kids but buyer = parents

Industry/Entity Type

Business

Requirements
Must have

• The label design should include:
- A place for my logo at the top (it is a simple logo with the text: The Maple Makery in Google Fonts type Dancing Script. There is a small flower as the dot of the i in Makery)
- You can use these colors: #eaeac5, #e5b7b7, #669899, #947057, #8cc1ba, #fbfaf3 or any other similar / complementary colors
- a placeholder for me to add in (through photoshop) a digital image of the actual craft that is included in the package
- a place where I can put a small description of the activity or point out some cool features of the project
- a place where I can indicate the age suitability of the product
- a place where I can detail a short description of the activity,what is included in the kit

Other requirements:
- my online store is similar to this one in design so you can visit this for inspiration on look and feel: http://bramble-muffin-hollow.shopwren.example/
- the files that you provide should allow me to resize the label if I need to change the dimensions of my packaging (vector preferred)
- the look and feel should be attractive for children but still professional and sticking to the look and feel for my online store

```html
<!DOCTYPE html>
<html lang="en">
<head>
<meta charset="utf-8">
<title>The Maple Makery – Kit Label</title>
<link href="https://fonts.googleapis.com/css2?family=Dancing+Script:wght@500&family=Montserrat:wght@400&display=swap" rel="stylesheet">
<style>
  :root {
    --page: #ffffff;
    --brand: #4f8a86;
    --frame: #a9c3c4;
    --cream: #f6f4de;
    --pattern-light: #e3eadf;
    --pattern-mid: #c9dad5;
    --tag: #a9c3c4;
    --tag-text: #3f6566;
    --rule: #c9d6d2;
    --leaf: #a0d4a1;
    --leaf-dark: #8cc78f;
  }
  * { margin: 0; padding: 0; box-sizing: border-box; }
  html, body { width: 857px; height: 1200px; overflow: hidden; background: var(--page); }
  .canvas { position: relative; width: 857px; height: 1200px; }

  .brand-name {
    position: absolute; top: 150px; left: 0; width: 100%;
    text-align: center;
    font-family: "Dancing Script", cursive;
    font-weight: 500; font-size: 62px; color: var(--brand);
  }

  .label {
    position: absolute; left: 229px; top: 337px; width: 405px; height: 672px;
    background: var(--frame); padding: 7px;
  }
  .label-inner {
    position: relative; width: 100%; height: 100%;
    background: var(--cream); border: 4px solid var(--cream);
    outline: 2px solid #ffffff; outline-offset: -6px;
  }
  .pattern {
    position: absolute;
    background:
      radial-gradient(circle at 50% 50%, var(--pattern-light) 0%, var(--pattern-mid) 100%);
  }
  .pattern-top { left: 0; top: 0; width: 100%; height: 20px; }
  .pattern-bottom { left: 0; bottom: 0; width: 100%; height: 24px; }
  .pattern-left { left: 0; top: 20px; width: 30px; bottom: 24px; }
  .pattern-right { right: 0; top: 20px; width: 30px; bottom: 24px; }
  .pattern-band { left: 0; top: 165px; width: 100%; height: 350px; }

  .field { position: absolute; left: 0; width: 100%; }
  .tag {
    display: block; width: 160px; margin-left: 103px;
    background: var(--tag); color: var(--tag-text);
    font-family: "Montserrat", sans-serif; font-size: 11px; letter-spacing: .5px;
    text-align: center; line-height: 20px; text-transform: uppercase;
  }
  .rule { height: 1px; background: var(--rule); margin: 14px 0 0 80px; width: 210px; }

  .field-description { top: 35px; }
  .field-ages { top: 112px; }
  .field-included { top: 523px; }

  .photo-frame {
    position: absolute; left: 32px; top: 195px; width: 326px; height: 290px;
    overflow: visible;
  }
  .photo-spot {
    position: absolute; left: 96px; top: 242px; width: 198px; height: 192px;
    background: var(--cream);
  }
</style>
</head>
<body>
<div class="canvas">
  <h1 class="brand-name">The Maple Makery</h1>

  <section class="label">
    <div class="label-inner">
      <div class="pattern pattern-top" role="img" aria-label="Soft teal lattice border pattern"></div>
      <div class="pattern pattern-left" role="img" aria-label="Soft teal lattice border pattern"></div>
      <div class="pattern pattern-right" role="img" aria-label="Soft teal lattice border pattern"></div>
      <div class="pattern pattern-band" role="img" aria-label="Soft teal lattice background pattern"></div>
      <div class="pattern pattern-bottom" role="img" aria-label="Soft teal lattice border pattern"></div>

      <div class="field field-description">
        <span class="tag">Description</span>
        <div class="rule"></div><div class="rule"></div><div class="rule"></div>
      </div>

      <div class="field field-ages">
        <span class="tag">Suitable for ages</span>
        <div class="rule"></div>
      </div>

      <svg class="photo-frame" viewBox="0 0 326 290" aria-hidden="true">
        <g fill="var(--leaf)">
          <rect x="20" y="20" width="286" height="250" rx="40"/>
          <circle cx="42" cy="34" r="30"/><circle cx="102" cy="20" r="30"/><circle cx="163" cy="16" r="30"/>
          <circle cx="224" cy="20" r="30"/><circle cx="284" cy="34" r="30"/>
          <circle cx="42" cy="256" r="30"/><circle cx="102" cy="270" r="30"/><circle cx="163" cy="274" r="30"/>
          <circle cx="224" cy="270" r="30"/><circle cx="284" cy="256" r="30"/>
          <circle cx="22" cy="92" r="28"/><circle cx="16" cy="145" r="28"/><circle cx="22" cy="198" r="28"/>
          <circle cx="304" cy="92" r="28"/><circle cx="310" cy="145" r="28"/><circle cx="304" cy="198" r="28"/>
        </g>
        <rect x="26" y="26" width="274" height="238" rx="58" fill="none" stroke="var(--cream)" stroke-width="3"/>
        <rect x="34" y="34" width="258" height="222" rx="50" fill="var(--leaf-dark)" opacity=".3"/>
      </svg>
      <div class="photo-spot" role="img" aria-label="Photo of the craft included in the kit"></div>

      <div class="field field-included">
        <span class="tag">Included in this kit</span>
        <div class="rule"></div><div class="rule"></div><div class="rule"></div><div class="rule"></div><div class="rule"></div>
      </div>
    </div>
  </section>
</div>
</body>
</html>
```